Briefpapier und Visitenkarten für Bayerisches Gasthaus mit Zimmer
Zielgruppe
Traditionelle Gaststätte im Zentrum einer Kleinstadt in Bayern. Direkt am Marktplatz. 10 Gästezimmer.
Bayerisch. Traditionell. Von junger Geschäftsführerin geführt, mit jungem Personal. Wir haben das Objekt erst vor Kurzem erworben und fangen gerade an.
Gerichte: Braten, Steaks, Brotzeiten, vegetarische und VEGANE Speisen
Getränke: Sehr bierlastig. Es war früher ein Brauereigasthaus. Heute gibts auch eine kleine feine Weinkarte.
Zielgruppe sind Einheimische und Touristen. Im Sommer kommen Radfahrer und Wanderer. Besonders angesprochen werden auch Kinder. Es gibt eine großzügige Spielecke.
Aufgabenstellung
Das Gasthaus heißt Eichel. Daher spielt der Eichel im Design auch eine wichtige Rolle.
Nachdem wir sehr familienorientiert sind, könnte ich mir auch eine Eichel-Familie vorstellen.
Visitenkarten und Briefpapier sollen alle wichtigen Infos enthalten, aber dabei sehr klar gehalten werden und nicht überladen sein. Mir ist ein schlichtes und ansprechendes Design wichtig. Es soll nicht verspielt sein.
Hier ist die Homepage:
www.eichel-gasthof-online.de
Info auf Briefpapier:
GASTHAUS EICHEL
Brennauer GmbH
Als Info auf Visitenkarte:
Gasthaus Eichel

```html
<!DOCTYPE html>
<html lang="de">
<head>
<meta charset="utf-8">
<title>Gasthaus Eichel – Visitenkarten</title>
<link rel="stylesheet" href="https://fonts.googleapis.com/css2?family=Didact+Gothic&display=swap">
<style>
  :root {
    --canvas: #dcdcdc;
    --dark-start: #101010;
    --dark-end: #363636;
    --green: #6b9630;
    --green-deep: #628a2c;
    --green-light: #7ba63a;
    --white: #ffffff;
    --grey-mid: #9a9a9a;
    --grey-soft: #bdbdbd;
    --grey-line: #5a5a5a;
    --text-light: #dddddd;
  }
  html, body {
    margin: 0;
    padding: 0;
    width: 1200px;
    height: 1200px;
    overflow: hidden;
    background: var(--canvas);
    font-family: "Didact Gothic", sans-serif;
  }
  .sheet {
    position: relative;
    width: 1200px;
    height: 1200px;
  }
  .card {
    position: absolute;
    width: 546px;
    height: 308px;
    overflow: hidden;
  }
  .card--front { left: 24px; }
  .card--back  { left: 600px; }
  .row-1 { top: 10px; }
  .row-2 { top: 338px; }
  .row-3 { top: 677px; }

  .theme-dark  { background: linear-gradient(90deg, var(--dark-start), var(--dark-end)); }
  .theme-light { background: var(--white); }
  .theme-green { background: linear-gradient(90deg, var(--green-deep), var(--green-light)); }

  /* brand mark placeholder */
  .brand-square {
    position: absolute;
    background: var(--green);
  }
  .card--front .brand-square { left: 45px; top: 18px; width: 104px; height: 104px; }
  .card--back  .brand-square { left: 30px; top: 198px; width: 66px; height: 66px; }
  .theme-green .brand-square { background: var(--white); }

  /* front wordmark */
  .wordmark {
    position: absolute;
    right: 8px;
    top: 188px;
    text-align: right;
  }
  .wordmark__name {
    display: block;
    font-size: 46px;
    line-height: 46px;
    color: var(--green);
  }
  .wordmark__place {
    display: block;
    font-size: 10.5px;
    line-height: 12px;
    color: var(--grey-mid);
    margin-top: 1px;
  }
  .divider {
    position: absolute;
    left: 235px;
    right: 8px;
    top: 266px;
    height: 1px;
    background: linear-gradient(90deg, var(--grey-line), var(--grey-mid));
  }
  .tagline {
    position: absolute;
    right: 8px;
    top: 270px;
    font-size: 31px;
    line-height: 34px;
    letter-spacing: 0.5px;
    color: var(--grey-mid);
    white-space: nowrap;
  }
  .theme-light .divider { background: linear-gradient(90deg, #444, #bbb); }
  .theme-green .wordmark__name,
  .theme-green .wordmark__place,
  .theme-green .tagline { color: var(--white); }
  .theme-green .divider { background: linear-gradient(90deg, rgba(255,255,255,0.3), var(--white)); }

  /* back contact block */
  .contact {
    position: absolute;
    right: 24px;
    top: 136px;
    text-align: right;
    font-size: 11px;
    line-height: 14px;
    color: var(--text-light);
  }
  .contact p { margin: 0 0 13px; }
  .contact .contact__name { color: var(--green-light); }
  .theme-light .contact { color: var(--grey-soft); }
  .theme-light .contact .contact__name { color: var(--green); }
  .theme-green .contact,
  .theme-green .contact .contact__name { color: var(--white); }
</style>
</head>
<body>
<main class="sheet">

  <!-- dark -->
  <section class="card card--front theme-dark row-1">
    <div class="brand-square" role="img" aria-label="Platz für das Eichel-Zeichen"></div>
    <div class="wordmark"><span class="wordmark__name">Eichel</span><span class="wordmark__place">Kornbach im Talgrund</span></div>
    <div class="divider"></div>
    <div class="tagline">GASTHAUS &amp; HOTEL</div>
  </section>
  <section class="card card--back theme-dark row-1">
    <div class="brand-square" role="img" aria-label="Platz für das Eichel-Zeichen"></div>
    <div class="contact">
      <p class="contact__name">Gasthaus Eichel<br>Kornbach im Talgrund</p>
      <p>Brennauer GmbH<br>Marktplatz 7<br>93999 Kornbach</p>
      <p>Tel. 09999 1234</p>
      <p>www.eichel-gasthof-online.de<br>info@eichel-gasthof-online.de</p>
    </div>
  </section>

  <!-- light -->
  <section class="card card--front theme-light row-2">
    <div class="brand-square" role="img" aria-label="Platz für das Eichel-Zeichen"></div>
    <div class="wordmark"><span class="wordmark__name">Eichel</span><span class="wordmark__place">Kornbach im Talgrund</span></div>
    <div class="divider"></div>
    <div class="tagline">GASTHAUS &amp; HOTEL</div>
  </section>
  <section class="card card--back theme-light row-2">
    <div class="brand-square" role="img" aria-label="Platz für das Eichel-Zeichen"></div>
    <div class="contact">
      <p class="contact__name">Gasthaus Eichel<br>Kornbach im Talgrund</p>
      <p>Brennauer GmbH<br>Marktplatz 7<br>93999 Kornbach</p>
      <p>Tel. 09999 1234</p>
      <p>www.eichel-gasthof-online.de<br>info@eichel-gasthof-online.de</p>
    </div>
  </section>

  <!-- green -->
  <section class="card card--front theme-green row-3">
    <div class="brand-square" role="img" aria-label="Platz für das Eichel-Zeichen"></div>
    <div class="wordmark"><span class="wordmark__name">Eichel</span><span class="wordmark__place">Kornbach im Talgrund</span></div>
    <div class="divider"></div>
    <div class="tagline">GASTHAUS &amp; HOTEL</div>
  </section>
  <section class="card card--back theme-green row-3">
    <div class="brand-square" role="img" aria-label="Platz für das Eichel-Zeichen"></div>
    <div class="contact">
      <p class="contact__name">Gasthaus Eichel<br>Kornbach im Talgrund</p>
      <p>Brennauer GmbH<br>Marktplatz 7<br>93999 Kornbach</p>
      <p>Tel. 09999 1234</p>
      <p>www.eichel-gasthof-online.de<br>info@eichel-gasthof-online.de</p>
    </div>
  </section>

</main>
</body>
</html>
```